Brisworth Electric Van Wrap 2023

We need a van wrap designed for our electrical company. We do residential and commercial work. We want the wrap be very eye catching. I want it to included our phone number and website, It must be easy to determine that we are a electrical company and remediable. this need to bee a full van wrap the van will be. the van is velko tarn cargomax cargo van 2021

Target Market(s)

Home owners that need electrical work done

Industry/Entity Type

Electrical services

Colors
0054AA
0677BA
7BADD7
CADEEF
E8F1F8

Requirements
Must have
• phone number- 850-555-0194 , website - www.brisworthelectric.example, included our logo and be very eye catching
Nice to have
• something that will stand out going do the road and know its a electrical company

```html
<!DOCTYPE html>
<html lang="en">
<head>
<meta charset="utf-8">
<title>Brisworth Electric Van Wrap</title>
<link rel="stylesheet" href="https://fonts.googleapis.com/css2?family=Anton&family=Montserrat:wght@700;800&display=swap">
<style>
  :root {
    --wrap-blue: #1ea7e1;
    --wrap-blue-deep: #0677ba;
    --wrap-white: #f3f4f5;
    --bolt-black: #141515;
    --ink-dark: #1d1f20;
    --text-white: #ffffff;
    --page: #ffffff;
  }
  html, body {
    margin: 0;
    width: 1200px;
    height: 1200px;
    overflow: hidden;
    background: var(--page);
  }
  .wrap-sheet {
    display: block;
    width: 1200px;
    height: 1200px;
  }
  .panel-base { fill: var(--wrap-white); stroke: #d6d8da; stroke-width: 2; }
  .blue-field { fill: url(#blueFade); }
  .slash-band { fill: var(--bolt-black); }
  .slash-gap { fill: var(--wrap-white); }
  .tagline {
    font-family: "Anton", sans-serif;
    font-size: 24px;
    fill: var(--ink-dark);
    letter-spacing: 0.5px;
  }
  .call-label {
    font-family: "Montserrat", sans-serif;
    font-weight: 800;
    font-size: 21px;
    fill: var(--text-white);
  }
  .phone-number {
    font-family: "Montserrat", sans-serif;
    font-weight: 800;
    font-size: 38px;
    fill: var(--text-white);
  }
  .web-address {
    font-family: "Anton", sans-serif;
    font-size: 20px;
    fill: var(--text-white);
    letter-spacing: 0.8px;
  }
  .phone-badge { fill: var(--text-white); }
  .phone-glyph { fill: var(--wrap-blue); }
  .brand-dot { fill: var(--wrap-blue); }
  .brand-name {
    font-family: "Montserrat", sans-serif;
    font-weight: 800;
    font-size: 26px;
    letter-spacing: 4px;
    fill: var(--wrap-blue-deep);
  }
</style>
</head>
<body>
<svg class="wrap-sheet" viewBox="0 0 1200 1200" xmlns="http://www.w3.org/2000/svg" aria-label="Brisworth Electric van wrap, driver and passenger sides">
  <defs>
    <linearGradient id="blueFade" x1="0" y1="0" x2="0" y2="1">
      <stop offset="0" stop-color="#22b0ea"/>
      <stop offset="1" stop-color="#0a92cf"/>
    </linearGradient>
    <g id="phoneIcon">
      <circle class="phone-badge" cx="0" cy="0" r="16"/>
      <path class="phone-glyph" d="M-8,-9 q3,-3 5,0 l3,5 q1,2 -1,4 l-2,2 q2,5 7,7 l2,-2 q2,-2 4,-1 l5,3 q3,2 0,5 l-3,3 q-3,2 -8,0 q-10,-5 -14,-14 q-2,-5 0,-8 z"/>
    </g>
  </defs>

  <g class="side side-passenger" transform="translate(100,140)">
    <rect class="panel-base" x="0" y="0" width="1000" height="340" rx="26"/>
    <path class="blue-field" d="M26,0 H600 L440,340 H26 Q0,340 0,314 V26 Q0,0 26,0 Z"/>
    <polygon class="slash-gap" points="600,0 616,0 456,340 440,340"/>
    <polygon class="slash-band" points="616,0 644,0 484,340 456,340"/>

    <text class="tagline" x="40" y="106" transform="skewX(-8)" transform-origin="40 106">LOCAL ELECTRICIANS YOU CAN TRUST!</text>
    <text class="call-label" x="92" y="146">CALL US</text>
    <use href="#phoneIcon" x="60" y="176"/>
    <text class="phone-number" x="88" y="190">850-555-0194</text>
    <text class="web-address" x="50" y="232">WWW.BRISWORTHELECTRIC.EXAMPLE</text>

    <circle class="brand-dot" cx="780" cy="130" r="44"/>
    <text class="brand-name" x="775" y="232" text-anchor="middle">BRISWORTH ELECTRIC</text>
  </g>

  <g class="side side-driver" transform="translate(100,700)">
    <rect class="panel-base" x="0" y="0" width="1000" height="340" rx="26"/>
    <path class="blue-field" d="M974,0 H400 L560,340 H974 Q1000,340 1000,314 V26 Q1000,0 974,0 Z"/>
    <polygon class="slash-gap" points="400,0 384,0 544,340 560,340"/>
    <polygon class="slash-band" points="384,0 356,0 516,340 544,340"/>

    <circle class="brand-dot" cx="220" cy="130" r="44"/>
    <text class="brand-name" x="225" y="232" text-anchor="middle">BRISWORTH ELECTRIC</text>

    <text class="tagline" x="962" y="106" text-anchor="end" transform="skewX(-8)" transform-origin="962 106">LOCAL ELECTRICIANS YOU CAN TRUST!</text>
    <text class="call-label" x="714" y="146">CALL US</text>
    <use href="#phoneIcon" x="682" y="176"/>
    <text class="phone-number" x="710" y="190">850-555-0194</text>
    <text class="web-address" x="960" y="232" text-anchor="end">WWW.BRISWORTHELECTRIC.EXAMPLE</text>
  </g>
</svg>
</body>
</html>
```